Fur Kit Hub Business Card Design Project

Hi All,

I need a business card /logo design.

The name of my upcoming business will be FurKitHub.example (e-commerce biz, thus name of business is same as website).

FurKitHub.example
Derek Lonsdale/Owner
tel# 555-017-4682
Brookvale, ME 00000

I'm definitely open to design creativity. However, one idea that I envisioned was to have a fun cartoon animals, like maybe a dog leaning on the 'P' and a cat leaning on the 'm' and a bird standing on the 't' or 'g'. Thank you in advance!

I need a catchy slogan added to my card. I appreciate your ideas. I don't want it to isolate dog or cat or bird etc...TY!

Hi All, The name of my upcoming business will be FurKitHub.example (e-commerce biz, thus name of business is same as website) I need a business card design/logo. Brookvale, ME 00000 tel# 555-017-4682 Derek Lonsdale/Owner I'm definitely open to design creativity. However, one idea that I envisioned was to have a fun cartoon animals, like maybe a dog leaning on the 'P' and a cat leaning on the 'm' and a bird standing on the 't' or 'g'. Thank you in advance!

Hi All! I need a catchy slogan added to my card. I appreciate your ideas. I don't want it to isolate dog or cat or bird etc...TY!

```html
<!DOCTYPE html>
<html lang="en">
<head>
<meta charset="utf-8">
<title>Fur Kit Hub – Business Card</title>
<link href="https://fonts.googleapis.com/css2?family=Tinos:wght@400;700&display=swap" rel="stylesheet">
<style>
  :root {
    --backdrop: #2b2b2b;
    --card-white: #ffffff;
    --band-green: #e3e99f;
    --ink: #111111;
    --art-blue: #7d9ee0;
    --art-blue-soft: #b9c9ee;
    --art-orange: #f2c44a;
    --art-orange-soft: #f7dc8a;
  }
  * { margin: 0; padding: 0; box-sizing: border-box; }
  html, body {
    width: 1200px; height: 899px; overflow: hidden;
    background: var(--backdrop);
  }
  .canvas {
    position: relative; width: 1200px; height: 899px;
    display: flex; align-items: center; justify-content: center;
  }
  .card {
    position: relative; width: 1000px; height: 572px;
    background: var(--card-white);
    overflow: hidden;
    font-family: "Tinos", "Times New Roman", serif;
    color: var(--ink);
  }
  .brand-band {
    position: absolute; left: 0; top: 0; width: 100%; height: 236px;
    background: var(--band-green);
  }
  .band-rule {
    position: absolute; left: 0; top: 246px; width: 100%; height: 6px;
    background: var(--band-green);
  }
  .art-dog-bird {
    position: absolute; left: 290px; top: 30px; width: 190px; height: 100px;
    border-radius: 40px;
    background: linear-gradient(90deg, var(--art-blue-soft), var(--art-blue));
  }
  .art-cat {
    position: absolute; left: 830px; top: 104px; width: 84px; height: 120px;
    border-radius: 34px;
    background: linear-gradient(180deg, var(--art-orange-soft), var(--art-orange));
  }
  .brand-name {
    position: absolute; left: 250px; top: 146px;
    white-space: nowrap;
    font-size: 70px; font-weight: 400; line-height: 1;
    letter-spacing: -1px;
  }
  .person {
    position: absolute; left: 130px; top: 312px;
    font-size: 34px; line-height: 1.15;
  }
  .person .role { display: block; padding-left: 16px; }
  .divider {
    position: absolute; left: 430px; top: 298px; width: 3px; height: 168px;
    background: var(--ink);
  }
  .contact {
    position: absolute; left: 470px; top: 314px;
    list-style: none;
    font-size: 27px; line-height: 1;
  }
  .contact li {
    display: flex; align-items: center; gap: 18px;
    height: 42px;
  }
  .contact svg { width: 24px; height: 24px; flex: none; fill: var(--ink); }
</style>
</head>
<body>
<main class="canvas">
  <section class="card">
    <div class="brand-band"></div>
    <div class="band-rule"></div>

    <div class="art-dog-bird" role="img" aria-label="Cartoon dog reading a paper beside a blue cartoon bird"></div>
    <div class="art-cat" role="img" aria-label="Cartoon orange cat holding a pencil"></div>

    <h1 class="brand-name">FurKitHub.example</h1>

    <p class="person">Derek Lonsdale<span class="role">Owner</span></p>

    <div class="divider"></div>

    <ul class="contact">
      <li>
        <svg viewBox="0 0 24 24" aria-hidden="true"><path d="M12 2 1 12h3v10h6v-6h4v6h6V12h3z"/></svg>
        Brookvale, ME 00000
      </li>
      <li>
        <svg viewBox="0 0 24 24" aria-hidden="true"><path d="M2 5h20v14H2z M2 5l10 8 10-8" fill="none" stroke="#111" stroke-width="2.4"/></svg>
        FurKitHub.example
      </li>
      <li>
        <svg viewBox="0 0 24 24" aria-hidden="true"><path d="M3 8c0-3 4-5 9-5s9 2 9 5v2h-5V8H8v2H3z M6 12h12l3 9H3z M10 14h4v4h-4z"/></svg>
        555-017-4682
      </li>
    </ul>
  </section>
</main>
</body>
</html>
```